Quality spirits brand needs a bottle design and logo

Designs look the same

We have received 3 designs. The font options for both of these were good, and we liked them. However, the image used wasn't strong enough. we want an image that speaks strongly in black and white, to do that it needs to be simplified some with less fine detail. We would also like to ensure some space is left for the type of spirit in the bottle i.e. RUM, SPICED RUM, VODKA, GIN

Please read the brief we have posted with the project closely to ensure you get a good understanding of what we are after.

```html
<!DOCTYPE html>
<html lang="en">
<head>
<meta charset="utf-8">
<title>Stray Bearing White Rum Label</title>
<link href="https://fonts.googleapis.com/css2?family=Bebas+Neue&family=Oswald:wght@400;500&family=Pinyon+Script&display=swap" rel="stylesheet">
<style>
  :root {
    --page: #ffffff;
    --navy: #2b2e55;
    --ink: #f1f1ef;
    --teal: #6cbcae;
    --rule: rgba(241, 241, 239, 0.85);
  }
  * { margin: 0; padding: 0; box-sizing: border-box; }
  html, body { width: 1200px; height: 1200px; overflow: hidden; background: var(--page); }
  .canvas { position: relative; width: 1200px; height: 1200px; }
  .label {
    position: absolute; left: 333px; top: 82px; width: 534px; height: 1035px;
    background: var(--navy); color: var(--ink); text-align: center;
  }
  .label > * { position: absolute; left: 0; width: 100%; }
  .border-band { height: 12px; }
  .border-band.top { top: 24px; }
  .border-band.bottom { top: 1000px; }
  .brand-name {
    top: 118px; font-family: "Bebas Neue", sans-serif; font-size: 92px;
    line-height: 1; letter-spacing: 1px; font-weight: 400;
  }
  .tagline {
    top: 232px; font-family: "Pinyon Script", cursive; font-size: 36px; line-height: 1;
  }
  .brand-mark { top: 318px; height: 220px; }
  .brand-mark-name {
    font-family: "Bebas Neue", sans-serif; font-size: 28px; letter-spacing: 1px;
  }
  .spirit-type {
    top: 608px; font-family: "Bebas Neue", sans-serif; font-size: 126px;
    line-height: 1; color: var(--teal); letter-spacing: 1px; font-weight: 400;
  }
  .details { top: 762px; height: 56px; }
  .details .value {
    position: absolute; top: 17px; font-family: "Oswald", sans-serif; font-size: 20px;
    line-height: 1; color: var(--ink);
  }
  .details .abv { left: 57px; }
  .details .volume { right: 57px; }
  .details .bottle-icon {
    position: absolute; left: 243px; top: 0; width: 48px; height: 56px;
    background: linear-gradient(180deg, rgba(241,241,239,0.55), rgba(241,241,239,0.25));
    border-radius: 4px;
  }
  .divider { top: 841px; height: 3px; }
  .motto {
    top: 868px; font-family: "Pinyon Script", cursive; font-size: 42px;
    line-height: 1; color: var(--teal);
  }
  .distillery {
    top: 928px; font-family: "Oswald", sans-serif; font-size: 16px;
    letter-spacing: 2.5px; line-height: 1;
  }
</style>
</head>
<body>
<div class="canvas">
  <section class="label">
    <svg class="border-band top" viewBox="0 0 534 12" preserveAspectRatio="none">
      <line x1="0" y1="2" x2="534" y2="2" stroke="var(--rule)" stroke-width="2"/>
      <line x1="0" y1="10" x2="534" y2="10" stroke="var(--rule)" stroke-width="2"/>
      <line x1="0" y1="6" x2="534" y2="6" stroke="var(--rule)" stroke-width="3" stroke-dasharray="40 14"/>
    </svg>

    <h1 class="brand-name">STRAY BEARING</h1>
    <p class="tagline">An Inspirational Spirit</p>

    <svg class="brand-mark" viewBox="0 0 534 220" role="img" aria-label="Stray Bearing brand mark">
      <circle cx="267" cy="110" r="96" fill="none" stroke="var(--ink)" stroke-width="10"/>
      <text class="brand-mark-name" x="267" y="120" text-anchor="middle" fill="var(--ink)">STRAY BEARING</text>
    </svg>

    <h2 class="spirit-type">WHITE RUM</h2>

    <div class="details">
      <svg width="534" height="56" viewBox="0 0 534 56" style="position:absolute;left:0;top:0">
        <g stroke="var(--rule)" stroke-width="2" stroke-dasharray="3 3">
          <line x1="50" y1="4" x2="150" y2="4"/>
          <line x1="50" y1="52" x2="150" y2="52"/>
          <line x1="384" y1="4" x2="484" y2="4"/>
          <line x1="384" y1="52" x2="484" y2="52"/>
        </g>
        <rect x="190" y="22" width="9" height="9" fill="var(--ink)"/>
        <rect x="335" y="22" width="9" height="9" fill="var(--ink)"/>
      </svg>
      <span class="value abv">40% ABV</span>
      <div class="bottle-icon" role="img" aria-label="Small illustration of a message in a bottle on waves"></div>
      <span class="value volume">700ml</span>
    </div>

    <svg class="divider" viewBox="0 0 534 3" preserveAspectRatio="none">
      <line x1="50" y1="1.5" x2="484" y2="1.5" stroke="var(--ink)" stroke-width="3"/>
    </svg>

    <p class="motto">Find Your Path to Adventure</p>
    <p class="distillery">STRAY BEARING DISTILLERY</p>

    <svg class="border-band bottom" viewBox="0 0 534 12" preserveAspectRatio="none">
      <line x1="0" y1="2" x2="534" y2="2" stroke="var(--rule)" stroke-width="2"/>
      <line x1="0" y1="10" x2="534" y2="10" stroke="var(--rule)" stroke-width="2"/>
      <line x1="0" y1="6" x2="534" y2="6" stroke="var(--rule)" stroke-width="3" stroke-dasharray="40 14"/>
    </svg>
  </section>
</div>
</body>
</html>
```